Maple Harbour Website

We are starting a marketing company and to do that we need a website! We want a website that will inspire and persuade to bring out the awesomeness in our clients.
What we want to see:
- Inspirational and persuasive imagery that relate to Branding.
- No cliche images eg. business man, suits and hand shakes
- We want to transform and educate our clients.
- We want to show them the path and would like our website to really act as a guide that guides them step by step through our process.
- We want the portray that we are an investment but not have a pretentious way to it. We put our heart into every project and that is how we treat our clients.
-When you submit your design please include what platform you have created for. Preference would be Wordpress or Joobla.

We have included the psd file for the wire frame, logo files, font files, site map and a link to a video we create to give you more information on what we would like to see. http://clipvault-example.com/t/qk82LmPzr

Feel free to make small modification to the logos if you think it will improve it. Your creativity and advice is most welcome.
Updates

One thing we forgot. We would like to have our contact information near the top of the website as well as at the bottom.  Here is out contact info:

Email: info@mapleharbour.ca
Phone: 403-555-0142

Reason: As we are new with the platform and that we want to optimize our results, we decided to extend the deadline by 15 days. Thanks!

Target Market(s)

28-60, Male and Female, Oil field, Local Businesses, Dentists, Chiropractors, Hair salon, Construction/Renovation, Events etc

Industry/Entity Type

Investment

Requirements
Must have
• - 4 Inspirational and persuasive Imagery for the top portion of the website
- Must have a feel as if your not on a website an example of this is linked below.
http://www.pixelforum-sample.com/design/472093/web-design-by-helen-dawes
Nice to have
• - Creative advice from you.
- Creative buttons for Get Free Quote and Subscribe buttons. Something out of the box that draws peoples attention. eg. a 'B' button. Just and example but still something related to branding.
Should not have
• No Cliches

```html
<!DOCTYPE html>
<html lang="en">
<head>
<meta charset="utf-8">
<title>Maple Harbour</title>
<link href="https://fonts.googleapis.com/css2?family=Open+Sans:wght@400;600;700&family=Francois+One&display=swap" rel="stylesheet">
<style>
:root{
  --green:#8cc63f;
  --green-dark:#4d8a1b;
  --green-deep:#3d7a12;
  --bg:#f7f7f7;
  --text:#666;
  --text-dark:#333;
  --grey:#8e8e8e;
  --grey-light:#e3e3e3;
  --footer-top:#8a8a8a;
  --footer-bottom:#2e2e2e;
  --white:#fff;
}
*{box-sizing:border-box;margin:0;padding:0}
html,body{width:1200px;height:912px;overflow:hidden;background:var(--bg);font-family:"Open Sans",sans-serif}
.page{position:relative;width:1200px;height:912px}
.topbar{position:absolute;left:0;top:0;width:1200px;height:37px;background:linear-gradient(#9bcf4a,#7fb82f)}
.contact{position:absolute;right:209px;display:flex;align-items:center;gap:6px;color:var(--white);font-weight:600;font-size:15px}
.topbar .contact{top:8px}
.contact svg{width:13px;height:13px}
.sidebar{position:absolute;left:208px;top:70px;width:192px;height:316px;background:linear-gradient(#f4f4f4,#e2e2e2);box-shadow:0 1px 4px rgba(0,0,0,.25)}
.logo{height:96px;padding:16px 12px 0;text-align:center}
.logo-name{display:flex;align-items:center;justify-content:center;gap:6px;font-weight:700;font-size:19px;color:var(--green-dark);letter-spacing:.5px}
.logo-name span.dot{width:10px;height:10px;border-radius:50%;background:var(--green)}
.tagline{margin-top:14px;font-size:11px;font-style:italic;color:#444;font-weight:600}
.nav a{display:block;height:31.2px;line-height:31px;padding-left:14px;font-size:13px;font-weight:700;color:var(--green-dark);text-decoration:none;border-bottom:1px solid #cfcfcf}
.connect-btn{position:absolute;left:0;bottom:0;width:192px;height:60px;background:linear-gradient(#8d8d8d,#bdbdbd);color:var(--white);font-family:"Francois One",sans-serif;font-size:20px;line-height:19px;text-align:center;padding-top:11px;letter-spacing:.5px}
.hero{position:absolute;left:400px;top:70px;width:600px;height:322px;background:radial-gradient(ellipse at 50% 40%,#c3de96 0%,#e7eedb 45%,#f3f3f3 75%)}
.step{position:absolute;width:76px;height:76px;border-radius:50%;background:radial-gradient(circle at 50% 35%,#a3a3a3,#787878);border:3px solid #6b6b6b;color:var(--white);font-weight:700;font-size:11.5px;line-height:14px;display:flex;align-items:center;justify-content:center;text-align:center;box-shadow:0 2px 3px rgba(0,0,0,.3)}
.step.active{background:radial-gradient(circle at 50% 35%,#9ed448,#78b426);border-color:#6aa51f}
.rule{position:absolute;left:212px;width:782px;border-top:1px dashed #aaa}
.social{position:absolute;left:209px;top:408px;display:flex;gap:7px}
.social span{width:42px;height:42px;background:linear-gradient(#555,#222)}
.tips{position:absolute;left:412px;top:411px}
.tips h3{font-weight:700;font-size:19px;color:var(--green);line-height:20px}
.tips p{font-weight:700;font-size:14.5px;color:#555;line-height:18px}
.email-field{position:absolute;left:628px;top:414px;width:268px;height:34px;background:var(--white);border:1px solid #ccc;font-size:12px;color:#777;padding:8px 7px}
.subscribe{position:absolute;left:900px;top:414px;width:94px;height:34px;background:linear-gradient(#bdbdbd,#8f8f8f);border:1px solid #999;border-radius:2px;color:var(--white);font-weight:700;font-size:14px;text-align:center;line-height:32px}
.content{position:absolute;left:212px;top:474px;width:782px}
.content h1{font-family:"Francois One",sans-serif;font-size:21px;color:var(--text-dark);font-weight:400;letter-spacing:.3px}
.content h2{margin-top:14px;font-size:13.5px;font-weight:700;color:var(--green-dark)}
.content p{font-size:13.5px;line-height:17.6px;color:var(--text);padding-left:1px}
.checks{list-style:none;margin-top:10px}
.checks li{display:flex;align-items:center;gap:9px;height:28.8px;font-size:13.5px;color:var(--text-dark)}
.checks svg{width:16px;height:16px;flex:none}
.content p.closing{margin-top:16px}
.quote{position:absolute;left:862px;top:684px;width:132px;height:33px;background:linear-gradient(#5ea625,#2f7010);border-radius:2px;color:var(--white);font-weight:700;font-size:13.5px;line-height:33px;text-align:center}
.footer{position:absolute;left:0;top:811px;width:1200px;height:101px;background:linear-gradient(var(--footer-top),var(--footer-bottom))}
.footer-links{position:absolute;left:211px;top:25px;display:flex;gap:11px;font-size:14.5px;color:var(--white)}
.copyright{position:absolute;left:211px;top:52px;font-size:14px;color:var(--green)}
.footer .contact{top:27px}
</style>
</head>
<body>
<div class="page">
  <header class="topbar">
    <div class="contact">
      <svg viewBox="0 0 14 14"><rect x="1" y="3" width="12" height="8" fill="#fff"/><path d="M1 3l6 5 6-5" fill="none" stroke="#555" stroke-width="1"/></svg>
      info@mapleharbour.ca&nbsp;|&nbsp;
      <svg viewBox="0 0 14 14"><path d="M3 1l3 3-2 2c1 2 2 3 4 4l2-2 3 3-2 2C6 13 1 8 1 3z" fill="#333"/></svg>
      403-555-0142
    </div>
  </header>

  <aside class="sidebar">
    <div class="logo">
      <div class="logo-name"><span class="dot"></span>MAPLE HARBOUR</div>
      <div class="tagline">Because You´re Awesome!</div>
    </div>
    <nav class="nav">
      <a>STRATEGY</a><a>PORTFOLIO</a><a>ABOUT US</a><a>CONTACT US</a><a>BLOG</a>
    </nav>
    <div class="connect-btn">CONNECT<br>WITH US</div>
  </aside>

  <div class="hero" role="img" aria-label="Illustration of green figures standing on linked platforms, a network of people growing together"></div>
  <div class="step" style="left:471px;top:311px">MAPLE<br>HARBOUR</div>
  <div class="step" style="left:600px;top:311px">BE<br>FOUND</div>
  <div class="step active" style="left:728px;top:311px">CONNECT</div>
  <div class="step" style="left:856px;top:311px">GET<br>GROWING</div>

  <div class="rule" style="top:399px"></div>
  <div class="social"><span></span><span></span><span></span><span></span></div>
  <div class="tips">
    <h3>GET TIPS AND TRICKS!</h3>
    <p>Subscribe to our Newsletter.</p>
  </div>
  <div class="email-field">your email id</div>
  <div class="subscribe">Subscribe</div>
  <div class="rule" style="top:462px"></div>

  <main class="content">
    <h1>WELCOME TO MAPLE HARBOUR</h1>
    <h2>Our Mission</h2>
    <p>Etiam adipiscing mollis nulla, ac bibendum elit commodo ac. Pellentesque vehicula sodales vulputate. Suspendisse vel semper tortor. Duis tristique pharetra ligula sed bibendum. Etiam adipiscing mollis nulla, ac bibendum elit commodo ac. Etiam adipiscing mollis nulla, ac bibendum elit commodo ac.</p>
    <ul class="checks">
      <li><svg viewBox="0 0 16 16"><rect width="16" height="16" rx="2" fill="#8cc63f"/><path d="M4 8l3 3 5-6" fill="none" stroke="#fff" stroke-width="2"/></svg>Nam ac risus metus, sit amet blandit ante.</li>
      <li><svg viewBox="0 0 16 16"><rect width="16" height="16" rx="2" fill="#8cc63f"/><path d="M4 8l3 3 5-6" fill="none" stroke="#fff" stroke-width="2"/></svg>Nunc adipiscing, ipsum eu scelerisque euismod, diam nisl condimentum neque,</li>
      <li><svg viewBox="0 0 16 16"><rect width="16" height="16" rx="2" fill="#8cc63f"/><path d="M4 8l3 3 5-6" fill="none" stroke="#fff" stroke-width="2"/></svg>Vel gravida ligula velit vitae nisl. Pellentesque at dignissim ipsum. Vivamus id massa arcu.</li>
      <li><svg viewBox="0 0 16 16"><rect width="16" height="16" rx="2" fill="#8cc63f"/><path d="M4 8l3 3 5-6" fill="none" stroke="#fff" stroke-width="2"/></svg>Phasellus feugiat condimentum neque ac bibendum.</li>
      <li><svg viewBox="0 0 16 16"><rect width="16" height="16" rx="2" fill="#8cc63f"/><path d="M4 8l3 3 5-6" fill="none" stroke="#fff" stroke-width="2"/></svg>Pellentesque dictum lectus sapien, eu pulvinar eros.</li>
    </ul>
    <p class="closing">Maecenas lacinia, nulla at interdum dapibus, velit sapien posuere eros, et hendrerit purus erat quis est. Proin commodo blandit mauris sed convallis. Donec tellus metus, feugiat sed condimentum congue, dignissim ut leo.</p>
  </main>
  <div class="quote">Get a Free Quote!</div>

  <footer class="footer">
    <div class="footer-links"><span>Site Map</span><span>Strategy</span><span>Portfolio</span><span>About Us</span><span>Contact Us</span><span>Blog</span></div>
    <div class="copyright">©MAPLE HARBOUR INC. 2013</div>
    <div class="contact">
      <svg viewBox="0 0 14 14"><rect x="1" y="3" width="12" height="8" fill="#fff"/><path d="M1 3l6 5 6-5" fill="none" stroke="#555" stroke-width="1"/></svg>
      info@mapleharbour.ca&nbsp;|&nbsp;
      <svg viewBox="0 0 14 14"><path d="M3 1l3 3-2 2c1 2 2 3 4 4l2-2 3 3-2 2C6 13 1 8 1 3z" fill="#222"/></svg>
      403-555-0142
    </div>
  </footer>
</div>
</body>
</html>
```